Book cover for publishing doctoral research about various national styles of piano playing.

I need a book cover for a publication of a doctoral research with regard to styles of piano performance characteristic to various nations.

Any images or graphics are optional, typography seems most important, but please feel free to be creative.

I attach the barcode, qsr and publisher's logo in the next few days. (Logo is still being designed).

For various reasons the size of the book is not completely decided yet. Please create your design in 7" x 10", but if at all possible, I would like to ask for files of two sizes, also including 8.5" x 11" in the final submission.

I am looking for a design that looks professional, probably simple, but I am open to any suggestions.

Dear Designers,I would like to thank you all for participation and submitting so many high-quality designs.My final decision was based on the feedback I received from my professional colleagues and potential readers.I would like to wish you all the best for the future.Best wishes,Tadeusz Added Monday, December 21, 2015

Pianists, students, music professionals

Publishing

• Title: Unfolding Seven Harbour Lullabies
• Subtitle: Memories and departures
• Author: Tadeusz Jarocki
• Space for my logo on the front page and the spine.
• On the back page, please include some space for a short biography, 'barcode' and 'qsr' code.
• Please include whatever else you consider necessary.
• Would it be possible to use the same cover to a e-book edition?

```html
<!DOCTYPE html>
<html lang="en">
<head>
<meta charset="utf-8">
<title>Unfolding Seven Harbour Lullabies — Book Cover</title>
<link rel="stylesheet" href="https://fonts.googleapis.com/css2?family=Poiret+One&family=Federo&display=swap">
<style>
  :root {
    --ink: #07090a;
    --paper: #ffffff;
    --gold: #cfa44e;
    --gold-light: #f0d27a;
    --gold-deep: #9c7528;
    --line: #111111;
  }
  * { margin: 0; padding: 0; box-sizing: border-box; }
  html, body { width: 1200px; height: 801px; overflow: hidden; background: var(--paper); }
  .cover { position: relative; width: 1200px; height: 801px; font-family: "Poiret One", sans-serif; }

  /* Back cover */
  .back { position: absolute; left: 0; top: 0; width: 560px; height: 801px; background: var(--paper); border: 1px solid #333; border-right: none; }
  .back__bar { position: absolute; left: 0; top: 0; width: 42px; height: 362px; background: var(--ink); }
  .back__rule { position: absolute; background: var(--line); }
  .back__rule--thin { left: 23px; top: 362px; width: 1.5px; height: 278px; }
  .back__rule--thick { left: 60px; top: 0; width: 3px; height: 640px; }
  .back__frame { position: absolute; left: 0; top: 0; }
  .placeholder { position: absolute; display: flex; align-items: center; justify-content: center; background: var(--paper); border: 1px solid #222; color: #000; font-family: Arial, Helvetica, sans-serif; }
  .back__logo { left: 24px; top: 738px; width: 50px; height: 42px; font-size: 8px; }
  .back__barcode { left: 408px; top: 711px; width: 116px; height: 69px; font-size: 9.5px; }

  /* Spine */
  .spine { position: absolute; left: 560px; top: 0; width: 80px; height: 801px; background: var(--ink); }
  .spine__title, .spine__author { position: absolute; left: 28px; writing-mode: vertical-rl; color: var(--gold); white-space: nowrap; }
  .spine__title { top: 40px; font-size: 25px; letter-spacing: 0.5px; }
  .spine__divider { position: absolute; left: 22px; top: 499px; width: 37px; height: 1px; background: var(--gold); }
  .spine__author { top: 528px; font-family: "Federo", sans-serif; font-size: 18px; font-variant: small-caps; letter-spacing: 1px; }
  .spine__logo { left: 18px; top: 739px; width: 50px; height: 41px; font-size: 8px; border: none; }

  /* Front cover */
  .front { position: absolute; left: 640px; top: 0; width: 560px; height: 801px; background: var(--ink); }
  .front__frame { position: absolute; left: 0; top: 0; }
  .front__logo { left: 30px; top: 22px; width: 72px; height: 59px; font-size: 11px; border: none; }
  .ornament { position: absolute; border-radius: 50%; background: radial-gradient(ellipse at center, var(--gold-light) 0%, var(--gold) 45%, rgba(207,164,78,0) 75%); opacity: 0.85; }
  .ornament--top { left: 214px; top: 156px; width: 140px; height: 40px; }
  .ornament--bottom { left: 214px; top: 352px; width: 140px; height: 40px; }
  .ornament--author-left { left: 152px; top: 748px; width: 34px; height: 16px; }
  .ornament--author-right { left: 382px; top: 748px; width: 34px; height: 16px; }
  .front__title { position: absolute; left: 60px; top: 205px; width: 450px; text-align: center; color: var(--gold); font-size: 44px; line-height: 44px; font-weight: 400; }
  .front__subtitle { position: absolute; left: 60px; top: 315px; width: 450px; display: flex; align-items: center; justify-content: center; gap: 10px; color: var(--gold); font-family: "Federo", sans-serif; font-size: 17px; text-transform: uppercase; letter-spacing: 0.5px; }
  .front__subtitle::before, .front__subtitle::after { content: ""; width: 28px; height: 5px; border-top: 1px solid var(--gold); border-bottom: 1px solid var(--gold); }
  .front__keyboard { position: absolute; left: 0; top: 538px; width: 560px; height: 180px; background: linear-gradient(180deg, #e9e9e9 0%, #ffffff 45%, #cfcfcf 100%); }
  .front__author { position: absolute; left: 60px; top: 742px; width: 450px; text-align: center; color: var(--gold); font-family: "Federo", sans-serif; font-size: 21px; font-variant: small-caps; letter-spacing: 1px; }
</style>
</head>
<body>
<main class="cover">

  <section class="back" aria-label="Back cover">
    <div class="back__bar"></div>
    <div class="back__rule back__rule--thin"></div>
    <div class="back__rule back__rule--thick"></div>
    <svg class="back__frame" width="560" height="801" viewBox="0 0 560 801" aria-hidden="true">
      <path d="M154 38 H458 A36 36 0 0 0 498 76 V496 A36 36 0 0 0 452 522 H141 A36 36 0 0 0 106 488 V69 A36 36 0 0 0 154 38 Z"
            fill="none" stroke="var(--gold)" stroke-width="2.5"/>
    </svg>
    <div class="placeholder back__logo">Your Logo</div>
    <div class="placeholder back__barcode">Space for Barcode</div>
  </section>

  <section class="spine" aria-label="Spine">
    <div class="spine__title">Unfolding Seven Harbour Lullabies</div>
    <div class="spine__divider"></div>
    <div class="spine__author">Tadeusz Jarocki</div>
    <div class="placeholder spine__logo">Your Logo</div>
  </section>

  <section class="front" aria-label="Front cover">
    <svg class="front__frame" width="560" height="801" viewBox="0 0 560 801" aria-hidden="true">
      <path d="M120 38 L484 40 Q488 92 536 98 V516" fill="none" stroke="var(--gold)" stroke-width="2"/>
      <path d="M30 94 V516" fill="none" stroke="var(--gold)" stroke-width="2"/>
      <path d="M30 726 V738 Q70 740 76 788 H482 Q490 742 536 738 V726" fill="none" stroke="var(--gold)" stroke-width="2"/>
    </svg>
    <div class="placeholder front__logo">Your Logo</div>

    <div class="ornament ornament--top" role="img" aria-label="Gold flourish ornament above the title"></div>
    <h1 class="front__title">Unfolding Seven<br>Harbour Lullabies</h1>
    <p class="front__subtitle">Memories and departures</p>
    <div class="ornament ornament--bottom" role="img" aria-label="Gold flourish ornament below the subtitle"></div>

    <div class="front__keyboard" role="img" aria-label="Illustration of a piano keyboard with black and white keys"></div>

    <div class="ornament ornament--author-left" role="img" aria-label="Small gold flourish"></div>
    <p class="front__author">Tadeusz Jarocki</p>
    <div class="ornament ornament--author-right" role="img" aria-label="Small gold flourish"></div>
  </section>

</main>
</body>
</html>
```